Business Card - Cooperate

Business Card for Larkfield Management Consulting

Target Market(s)

Corparte - b2B

Industry/Entity Type

Management Consulting - Professional Services

Contact Information for Business Card

Company Name , Slogan , Dummy Address,

Requirements
Must have
• Reach your Full Potential

```html
<!DOCTYPE html>
<html lang="en">
<head>
<meta charset="utf-8">
<title>Larkfield Management Consulting — Business Card</title>
<link href="https://fonts.googleapis.com/css2?family=Ubuntu:wght@400;500;700&display=swap" rel="stylesheet">
<style>
  :root {
    --backdrop: #dcdde1;
    --navy-deep: #241a58;
    --navy: #33336f;
    --periwinkle: #5b78b5;
    --brand-blue: #2f4fa5;
    --teal: #17958a;
    --green: #3fb24a;
    --ink: #3b3b3b;
    --ink-soft: #4a4a4a;
    --paper: #ffffff;
    --paper-shade: #efefef;
  }
  * { margin: 0; padding: 0; box-sizing: border-box; }
  html, body {
    width: 1200px; height: 800px; overflow: hidden;
    background: var(--backdrop);
    font-family: "Ubuntu", sans-serif;
  }
  .card {
    position: absolute;
    left: 390px;
    width: 420px; height: 240px;
    border-radius: 10px;
    overflow: hidden;
  }
  .card--front {
    top: 130px;
    background: linear-gradient(30deg, var(--navy-deep) 0%, var(--navy) 40%, #4a5b9c 70%, var(--periwinkle) 100%);
    color: var(--paper);
  }
  .card--back {
    top: 430px;
    background: linear-gradient(160deg, var(--paper-shade) 0%, var(--paper) 60%, #f6f6f6 100%);
  }
  .brand {
    position: absolute;
    display: flex; flex-direction: column; align-items: flex-start;
  }
  .brand__row { display: flex; align-items: center; gap: 10px; }
  .brand__dot { border-radius: 50%; flex: none; }
  .brand__name { font-weight: 500; line-height: 1; letter-spacing: 0.5px; }
  .brand__tagline {
    font-weight: 700; text-transform: uppercase; white-space: nowrap;
  }
  .card--front .brand { left: 87px; top: 88px; }
  .card--front .brand__dot { width: 54px; height: 54px; background: var(--paper); }
  .card--front .brand__name { font-size: 44px; color: var(--paper); }
  .card--front .brand__tagline {
    font-size: 9px; letter-spacing: 2px; color: var(--paper);
    margin: 2px 0 0 64px;
  }
  .card--back .brand { right: 30px; top: 30px; }
  .card--back .brand__dot { width: 40px; height: 40px; background: var(--brand-blue); }
  .card--back .brand__name { font-size: 32px; color: var(--brand-blue); }
  .card--back .brand__tagline {
    font-size: 6.5px; letter-spacing: 1.6px; color: var(--teal);
    margin: 3px 0 0 50px;
  }
  .holder { position: absolute; left: 28px; top: 118px; right: 24px; }
  .holder__name { font-size: 23px; font-weight: 500; color: var(--ink); line-height: 1.1; }
  .holder__role {
    display: flex; align-items: center; gap: 4px;
    font-size: 15px; color: var(--teal); margin-top: 1px;
  }
  .holder__rule { flex: 1; height: 1px; background: var(--teal); margin-top: 8px; }
  .contact {
    position: absolute; left: 28px; top: 186px;
    display: flex; gap: 14px;
    font-size: 11px; color: var(--ink-soft); line-height: 13px;
  }
  .contact__group { display: flex; flex-direction: column; }
  .contact__item { display: flex; align-items: center; gap: 4px; white-space: nowrap; }
  .contact__item svg { width: 9px; height: 9px; flex: none; }
  .contact__item--plain { padding-left: 13px; }
  .contact__group--address { margin-left: 6px; }
  .accent-band {
    position: absolute; left: 0; right: 0; bottom: 0; height: 15px;
    background: linear-gradient(90deg, var(--navy-deep) 0%, #2b3a84 35%, #3765a8 55%, #3d9e78 80%, var(--green) 100%);
  }
</style>
</head>
<body>
  <section class="card card--front" aria-label="Card front">
    <div class="brand">
      <div class="brand__row">
        <span class="brand__dot"></span>
        <span class="brand__name">Larkfield</span>
      </div>
      <span class="brand__tagline">Reach your full potential</span>
    </div>
  </section>

  <section class="card card--back" aria-label="Card back">
    <div class="brand">
      <div class="brand__row">
        <span class="brand__dot"></span>
        <span class="brand__name">Larkfield</span>
      </div>
      <span class="brand__tagline">Reach your full potential</span>
    </div>

    <div class="holder">
      <h1 class="holder__name">Miles Hartwell</h1>
      <div class="holder__role"><span>Managing Partner</span><span class="holder__rule"></span></div>
    </div>

    <div class="contact">
      <div class="contact__group">
        <span class="contact__item">
          <svg viewBox="0 0 10 10" aria-hidden="true"><path d="M2 1l2 2-1 1.2c.6 1.2 1.6 2.2 2.8 2.8L7 6l2 2-1.2 1.2C4.5 9 1 5.5.8 2.2z" fill="none" stroke="#17958a" stroke-width=".9"/></svg>
          (555) 214-3380
        </span>
        <span class="contact__item">
          <svg viewBox="0 0 10 10" aria-hidden="true"><rect x="2.5" y="1" width="5" height="3" fill="#17958a"/><rect x="1" y="4" width="8" height="3.5" rx=".6" fill="#17958a"/><rect x="2.5" y="6.5" width="5" height="2.5" fill="#17958a"/></svg>
          (555) 640-1928
        </span>
      </div>
      <div class="contact__group">
        <span class="contact__item">
          <svg viewBox="0 0 10 10" aria-hidden="true"><rect x="1" y="2.5" width="8" height="5.5" fill="#17958a"/><path d="M1 2.5l4 3 4-3" fill="none" stroke="#fff" stroke-width=".8"/></svg>
          info@larkfield.com
        </span>
        <span class="contact__item">
          <svg viewBox="0 0 10 10" aria-hidden="true"><circle cx="5" cy="5" r="4" fill="none" stroke="#17958a" stroke-width=".9"/><path d="M5 1c-1.5 1.5-1.5 6.5 0 8M5 1c1.5 1.5 1.5 6.5 0 8M1 5h8" fill="none" stroke="#17958a" stroke-width=".7"/></svg>
          www.larkfield.com
        </span>
      </div>
      <div class="contact__group contact__group--address">
        <span class="contact__item">
          <svg viewBox="0 0 10 10" aria-hidden="true"><path d="M5 9.5S1.8 6 1.8 3.8a3.2 3.2 0 016.4 0C8.2 6 5 9.5 5 9.5z" fill="none" stroke="#17958a" stroke-width=".9"/><circle cx="5" cy="3.8" r="1.1" fill="#17958a"/></svg>
          480 Harbor Crest Avenue
        </span>
        <span class="contact__item" style="padding-left:1px">Coral Bay, FL 33410</span>
      </div>
    </div>

    <div class="accent-band"></div>
  </section>
</body>
</html>
```